Wordpress Lifestyle Blog

Just to be clear - I have the domain and the wordpress site (which is messy). I need someone to help me complete a simple blog design and then go into the existing wordpress site, and get rid of all the existing rubbish and set up the templates please. If we progress with design can we please be clear about additional costs upfront which, of course, I appreciate is the case.

Need a lifestyle blog. It is called brightyearsahead.com. Aimed at the older woman but needs to look fresh and young, not old fashioned. Navigation will be Home, Fashion, Feelings, Fitness, Contact. I have a logo but not sure it will work at the moment so happy with stylised words.Will have social media links.

Need homepage (not overly long) to have a main slider for pics/videos. Then the three category boxes underneath linking through to 2nd level pages containing blogs for that category and then the actual blog page. Happy to be led by expertise if this is not gonna work.

Am really looking for something clean and fresh like a Marwyn type approach to be honest.

If you need any further direction please just ask - once design chosen I am looking to move quickly.

Thank you so much for looking at this brief

Target Market(s)

Women, 40 - 60 age group but with a younger outlook

Number of Pages Required

3 page

Colors

Designer to choose colors to be used in the design.

Requirements
Must have
• Reflect youth, fun, bright
• Lift easily into a wordpress format
Should not have
• Old, staid, frumpy,dark

```html
<!DOCTYPE html>
<html lang="en">
<head>
<meta charset="utf-8">
<title>Bright Years Ahead – Latest Posts</title>
<link href="https://fonts.googleapis.com/css2?family=Libre+Caslon+Text:wght@400&family=Mulish:wght@300;400;600&display=swap" rel="stylesheet">
<style>
  :root {
    --page-bg: #ffffff;
    --title-ink: #4a4747;
    --body-ink: #6e6b6b;
    --date-ink: #9a9696;
    --rule: #5a5757;
    --accent: #e6ccad;
    --accent-fill: #ead3b8;
    --soft-btn: #f2efec;
    --field-border: #4f4c4c;
  }
  * { box-sizing: border-box; margin: 0; padding: 0; }
  html, body {
    width: 1200px; height: 800px; overflow: hidden;
    background: var(--page-bg);
    font-family: "Mulish", Arial, sans-serif;
    color: var(--body-ink);
  }
  .page { position: relative; width: 1200px; height: 800px; }

  /* Post list */
  .post { position: absolute; left: 112px; width: 643px; height: 183px; }
  .post--first { top: 56px; }
  .post--second { top: 275px; }
  .post--third { top: 494px; }
  .post-thumb { position: absolute; left: 0; top: 0; width: 264px; height: 183px; }
  .post-body { position: absolute; left: 290px; top: -9px; width: 353px; }
  .post-title {
    font-family: "Libre Caslon Text", Georgia, serif;
    font-weight: 400; font-size: 21px; line-height: 35px;
    color: var(--title-ink);
  }
  .post-excerpt {
    font-weight: 300; font-size: 16px; line-height: 28px;
    margin-top: 11px; width: 330px;
  }
  .post-date {
    font-weight: 600; font-size: 14.5px; line-height: 20px; color: var(--date-ink);
    margin-top: 18px;
  }
  .post-rule { position: absolute; left: 112px; width: 643px; height: 0; border-top: 1px solid var(--rule); }
  .post-rule--first { top: 256px; }
  .post-rule--second { top: 475px; }
  .view-all {
    position: absolute; left: 112px; top: 703px;
    width: 176px; height: 55px;
    background: var(--soft-btn); border: none;
    font-family: "Mulish", Arial, sans-serif; font-weight: 300;
    font-size: 19px; color: var(--body-ink); letter-spacing: 0.3px;
  }

  /* Sidebar */
  .author { position: absolute; left: 781px; top: 0; width: 308px; height: 800px; text-align: center; }
  .author > * { position: absolute; left: 0; width: 308px; }
  .author-photo {
    left: 64px; width: 180px; height: 180px; top: 57px; border-radius: 50%;
    background: radial-gradient(circle at 50% 55%, #c99a83 0%, #8a6a60 45%, #2f2a2c 80%);
  }
  .social { top: 265px; display: flex; justify-content: center; gap: 14px; list-style: none; }
  .social li { font-size: 13px; line-height: 20px; font-weight: 600; color: var(--title-ink); }
  .author-name {
    top: 312px; font-size: 31px; line-height: 38px; font-weight: 400;
    color: var(--accent); letter-spacing: 0.5px;
  }
  .author-bio { top: 369px; font-size: 16px; line-height: 27.5px; font-weight: 300; }
  .newsletter-title { top: 485px; font-size: 30px; line-height: 38px; font-weight: 400; color: var(--accent); }
  .newsletter { top: 552px; }
  .email-field {
    display: block; width: 308px; height: 55px;
    border: 1.5px solid var(--field-border); background: #fff;
    font-family: "Mulish", Arial, sans-serif; font-weight: 300;
    font-size: 19px; color: var(--body-ink); text-align: center;
  }
  .email-field::placeholder { color: var(--body-ink); }
  .send-btn {
    display: block; width: 308px; height: 55px; margin-top: 24px;
    background: var(--accent-fill); border: none; color: #fff;
    font-family: "Mulish", Arial, sans-serif; font-weight: 400; font-size: 22px;
    letter-spacing: 0.5px;
  }
</style>
</head>
<body>
<main class="page">
  <section class="post-list">
    <article class="post post--first">
      <div class="post-thumb" role="img" aria-label="Photo of two women walking together, one in a checked blazer, one in a red floral dress"
           style="background: linear-gradient(90deg, #b9b7b2 0%, #8a8f96 35%, #c94a45 70%, #bfc2c3 100%);"></div>
      <div class="post-body">
        <h2 class="post-title">How To Wear Skinny Jeans When<br>You’re Not Exactly Skinny</h2>
        <p class="post-excerpt">Lorem ipsum dolor sit amet, consectetur adipiscing elit. Sed nisl leo, aliquet</p>
        <p class="post-date">26th April 2018</p>
      </div>
    </article>
    <div class="post-rule post-rule--first"></div>
    <article class="post post--second">
      <div class="post-thumb" role="img" aria-label="Photo of four friends in white summer dresses and straw hats"
           style="background: linear-gradient(90deg, #7c8a5e 0%, #e8e2d6 30%, #f3efe8 60%, #8f9a6a 100%);"></div>
      <div class="post-body">
        <h2 class="post-title">The Best Dress I’ve Bought<br>In Ages</h2>
        <p class="post-excerpt">Lorem ipsum dolor sit amet, consectetur adipiscing elit. Sed nisl leo, aliquet</p>
        <p class="post-date">26th April 2018</p>
      </div>
    </article>
    <div class="post-rule post-rule--second"></div>
    <article class="post post--third">
      <div class="post-thumb" role="img" aria-label="Photo of a woman riding a bicycle with a basket under blossom trees"
           style="background: linear-gradient(160deg, #e8c9cf 0%, #d9b3b8 35%, #a7b08e 65%, #d7d4cf 100%);"></div>
      <div class="post-body">
        <h2 class="post-title">How To Wear Skinny Jeans When<br>You’re Not Exactly Skinny</h2>
        <p class="post-excerpt">Lorem ipsum dolor sit amet, consectetur adipiscing elit. Sed nisl leo, aliquet</p>
        <p class="post-date">26th April 2018</p>
      </div>
    </article>
  </section>
  <button class="view-all" type="button">VIEW ALL</button>

  <aside class="author">
    <div class="author-photo" role="img" aria-label="Portrait photo of the blog author"></div>
    <ul class="social">
      <li>Loop</li><li>Chirpy</li><li>Lens</li><li>Board</li>
    </ul>
    <h3 class="author-name">JOANNA DOE</h3>
    <p class="author-bio">Lorem ipsum dolor sit amet, consectetur<br>adipiscing elit. Sed nisl leo,<br>aliquet</p>
    <h3 class="newsletter-title">Stay in Touch</h3>
    <form class="newsletter">
      <input class="email-field" type="email" placeholder="Your Email">
      <button class="send-btn" type="button">SEND</button>
    </form>
  </aside>
</main>
</body>
</html>
```